Newsletter-Design für Garten-Samen Shop
Zielgruppe
Online Shop für Obst-, Gemüse-, Kräuter- und Pflanzensamen
Aufgabenstellung
www.beetfreunde-portal.example ist die Seite mit den Produkten. Als Tipp sollte das Jiaogulan genannt werden da dieses Produkt sich am meisten verkauft.

```html
<!DOCTYPE html>
<html lang="de">
<head>
<meta charset="utf-8">
<title>Newsletter – Beetfreunde</title>
<link href="https://fonts.googleapis.com/css2?family=Open+Sans:wght@300;400;600&display=swap" rel="stylesheet">
<style>
  :root {
    --backdrop: #e4e4e4;
    --peach: #eb9a72;
    --peach-light: #f2b08e;
    --peach-glass: rgba(238, 150, 108, 0.82);
    --white: #ffffff;
    --photo-green: #3f6b34;
    --photo-apple: #f1e6d8;
    --photo-red: #b6524a;
    --photo-wood: #6e3a30;
  }
  * { box-sizing: border-box; margin: 0; padding: 0; }
  html, body { width: 1200px; height: 848px; overflow: hidden; }
  body {
    background: var(--backdrop);
    font-family: "Open Sans", Arial, sans-serif;
    color: var(--white);
    position: relative;
  }
  .flyer {
    position: absolute;
    left: 110px; top: 84px;
    width: 980px; height: 680px;
    background: var(--peach);
    overflow: hidden;
    box-shadow: 0 10px 30px rgba(0,0,0,0.18);
  }
  .flyer__photo {
    position: absolute;
    left: 0; top: 0;
    width: 560px; height: 100%;
    background:
      linear-gradient(180deg, #5a6a5a 0%, var(--photo-green) 22%, var(--photo-apple) 38%, #e7c7b3 55%, var(--photo-red) 72%, var(--photo-wood) 100%);
  }
  .flyer__top-panel {
    position: absolute;
    left: 360px; top: 0;
    width: 620px; height: 150px;
    background: linear-gradient(90deg, var(--peach-light), var(--peach));
  }
  .shop-name {
    position: absolute;
    left: 400px; top: 38px;
    font-size: 20px; font-weight: 600;
    letter-spacing: 0.2px;
  }
  .shop-claim {
    position: absolute;
    left: 400px; top: 72px;
    width: 220px;
    font-size: 12px; font-weight: 300; line-height: 1.35;
  }
  .headline-box {
    position: absolute;
    left: 300px; top: 168px;
    width: 600px; height: 140px;
    border: 3px solid var(--white);
    background: var(--peach-glass);
    display: flex; align-items: center; justify-content: center;
  }
  .headline {
    font-size: 30px; font-weight: 600; line-height: 1.25;
    text-align: center;
  }
  .tip {
    position: absolute;
    left: 620px; top: 340px;
    width: 330px;
  }
  .tip__label { position: absolute; left: 0; top: 0; width: 230px; height: 200px; }
  .tip__label text { fill: var(--white); font-size: 17px; font-weight: 300; font-family: "Open Sans", Arial, sans-serif; }
  .tip__image {
    position: absolute;
    left: 60px; top: 30px;
    width: 150px; height: 150px;
    border-radius: 50%;
    border: 3px solid var(--white);
    background: radial-gradient(circle at 45% 45%, #a8cf8a 0%, #5f9c45 55%, #2f6b2a 100%);
  }
  .tip__name {
    position: absolute;
    left: 0; top: 200px;
    font-size: 22px; font-weight: 400;
  }
  .tip__subtitle {
    position: absolute;
    left: 0; top: 232px;
    font-size: 13px; font-weight: 300;
  }
  .tip__text {
    position: absolute;
    left: 0; top: 260px;
    width: 330px;
    font-size: 13px; font-weight: 300; line-height: 1.45;
  }
</style>
</head>
<body>
  <article class="flyer">
    <div class="flyer__photo" role="img" aria-label="Foto: geschnittene Äpfel, Karotten und Kräuter auf einem Holzbrett"></div>
    <div class="flyer__top-panel"></div>
    <p class="shop-name">www.beetfreunde-portal.example</p>
    <p class="shop-claim">Ihr Onlineshop für Obst-, Gemüse-, Kräuter- und Pflanzensamen</p>

    <div class="headline-box">
      <h1 class="headline">Das beste Obst und Gemüse<br>kommt aus dem eigenen Garten</h1>
    </div>

    <section class="tip">
      <svg class="tip__label" viewBox="0 0 230 200" aria-hidden="true">
        <defs><path id="tipArc" d="M 70 160 A 88 88 0 0 1 120 24"/></defs>
        <text><textPath href="#tipArc">Unser Tipp!</textPath></text>
      </svg>
      <div class="tip__image" role="img" aria-label="Foto: grüne Blätter der Jiaogulan-Pflanze"></div>
      <h2 class="tip__name">Jiaogulan</h2>
      <p class="tip__subtitle">– Das Kraut der Unsterblichkeit</p>
      <p class="tip__text">Das Superfood verbessert die Nährstoff-Versorgung aller Organe, sowie die Herzleistung und die Blutzirkulation.</p>
    </section>
  </article>
</body>
</html>
```